Label for Olive Oil Bottle TESQUINA

Dear Designers,
The task is to create a label for an Olive Oil Bottle for the Tesquina Brand.
Please see the attached files for the information that must appear on the label.
Please produce the label in three different colour schemes: Red for the BRUMO version of the label,
Blue for the VELTA version and light green for the MERIDINO version of the label.
Please present the label on photorealistic bottle bock-ups like shown in the file attached.
It is not necessary to use the same template but it must be similar.

Target Market(s)

Germany, Austria and Swizerland

Industry/Entity Type

Food Production

Font styles to use
Serif
Script

Requirements
Must have
• a) Please produce 3 different versions of the label:
• 1. BRUMO
• 2. VELTA
• 3. MERIDINO
• b) Please use for the presentation of the labels the bottles in the attached file.
• They are in big scale so feel free to scale them down
• c) Please present the label on a white/transparent background
• d) Please fint the information for the labels on the files attached
Nice to have
• - Please see the file example.pdf to have a ROUGH idea how the design COULD be.
• - The label/mockup should be presented on a white/transparent background
Should not have
• Ill tell you...

```html
<!DOCTYPE html>
<html lang="de">
<head>
<meta charset="utf-8">
<title>Tesquina Olio di oliva – Etiketten</title>
<link rel="stylesheet" href="https://fonts.googleapis.com/css2?family=Old+Standard+TT:wght@400;700&family=Yellowtail&family=Tinos:wght@400;700&display=swap">
<style>
  :root {
    --page: #ffffff;
    --frame-line: #4f5226;
    --frame-cream: #f2ecc4;
    --green-a: #c3cf55;
    --green-b: #a9bb3a;
    --red-a: #e06149;
    --red-b: #c9402f;
    --blue-a: #bdeff5;
    --blue-b: #3fb9d2;
    --ink: #1f1f1f;
    --white: #ffffff;
    --pale-yellow: #f0ec8c;
    --soft-yellow: #ece87a;
    --accent-red: #d9303a;
    --gold: #c9a640;
  }
  * { box-sizing: border-box; margin: 0; padding: 0; }
  html, body { width: 1181px; height: 1200px; overflow: hidden; background: var(--page); }
  .label-row { position: relative; width: 1181px; height: 1200px; }

  .label { position: absolute; top: 405px; width: 240px; height: 630px; text-align: center; }
  .label--meridino-green { left: 88px; }
  .label--brumo-red { left: 448px; }
  .label--velta-blue { left: 830px; }
  .label__frame { position: absolute; inset: 0; width: 240px; height: 630px; }
  .label__content { position: absolute; inset: 0; }

  .brand {
    position: absolute; top: 62px; left: 0; right: 0;
    display: flex; align-items: center; justify-content: center; gap: 7px;
    font-family: "Old Standard TT", serif; font-weight: 700; font-size: 24px;
    letter-spacing: 0.5px; color: var(--accent-red);
  }
  .brand__dot { width: 10px; height: 10px; border-radius: 50%; background: var(--accent-red); }

  .title { position: absolute; left: 0; right: 0; font-family: "Yellowtail", cursive; line-height: 1; }
  .title--olio { top: 148px; font-size: 62px; color: var(--white); }
  .title--sub { top: 218px; font-size: 16px; padding-left: 70px; color: var(--soft-yellow); }
  .title--dioliva { top: 238px; font-size: 34px; color: var(--white); }
  .label--brumo-red .title--dioliva { top: 222px; }
  .label--velta-blue .title--olio { color: var(--soft-yellow); }

  .branch {
    position: absolute; top: 300px; left: 36px; width: 168px; height: 130px;
    border-radius: 50%;
    background: radial-gradient(ellipse at center, #93ab5e 0%, rgba(111,138,85,0.55) 55%, rgba(111,138,85,0) 72%);
  }

  .rule { position: absolute; left: 22px; right: 22px; height: 1px; background: var(--gold); }
  .rule--top { top: 446px; }
  .rule--bottom { top: 488px; }

  .variant {
    position: absolute; top: 452px; left: 0; right: 0;
    font-family: "Old Standard TT", serif; font-weight: 700; font-size: 27px; letter-spacing: 1px;
  }
  .label--meridino-green .variant { color: var(--accent-red); font-size: 24px; }
  .label--brumo-red .variant { color: var(--white); }
  .label--velta-blue .variant { color: var(--ink); }

  .legal {
    position: absolute; top: 494px; left: 0; right: 0;
    font-family: "Tinos", serif; font-weight: 700; font-size: 9.5px; line-height: 1.05; color: var(--ink);
  }
  .label--brumo-red .legal { color: var(--pale-yellow); font-weight: 400; }
  .label--velta-blue .legal { color: var(--accent-red); font-weight: 400; }

  .mild {
    position: absolute; top: 520px; left: 0; right: 0;
    font-family: "Old Standard TT", serif; font-weight: 700; font-size: 13px; color: var(--ink);
  }

  .usage {
    position: absolute; top: 520px; left: 30px; right: 30px; height: 22px;
    font-family: "Tinos", serif; font-size: 15px; line-height: 22px; letter-spacing: 0.5px;
    background: var(--accent-red); color: var(--white);
  }
  .label--brumo-red .usage { background: var(--pale-yellow); color: var(--ink); top: 526px; }
  .label--velta-blue .usage { top: 536px; }

  .footer {
    position: absolute; top: 566px; left: 34px; right: 34px;
    display: flex; align-items: center; justify-content: space-between;
    font-family: "Tinos", serif; font-size: 11px; color: var(--ink);
  }
  .footer__small { font-size: 8px; }
  .footer__stars { color: var(--accent-red); font-size: 8px; letter-spacing: 1px; }
  .label--velta-blue .footer__stars { color: var(--ink); }
  .label--brumo-red .footer { color: var(--pale-yellow); }
  .label--brumo-red .footer__stars { color: var(--pale-yellow); }
  .footer__sprig { width: 20px; height: 18px; border-radius: 50%; background: var(--accent-red); opacity: 0.75; }
  .label--brumo-red .footer__sprig { background: var(--pale-yellow); }
  .label--velta-blue .footer__sprig { background: var(--ink); }
</style>
</head>
<body>
<main class="label-row">

  <!-- Green MERIDINO -->
  <section class="label label--meridino-green">
    <svg class="label__frame" viewBox="0 0 240 630" aria-hidden="true">
      <defs>
        <linearGradient id="panel-green" x1="0" x2="1">
          <stop offset="0" stop-color="var(--green-b)"/><stop offset="0.5" stop-color="var(--green-a)"/><stop offset="1" stop-color="var(--green-b)"/>
        </linearGradient>
      </defs>
      <path d="M50 40 Q60 30 70 30 Q100 0 120 0 Q140 0 170 30 Q180 30 190 40 L222 40 Q222 52 234 52 L234 578 Q222 578 222 590 L190 590 Q180 600 170 600 Q140 630 120 630 Q100 630 70 600 Q60 600 50 590 L18 590 Q18 578 6 578 L6 52 Q18 52 18 40 Z" fill="var(--frame-cream)" stroke="var(--frame-line)" stroke-width="3"/>
      <path d="M56 50 Q64 42 74 42 Q102 14 120 14 Q138 14 166 42 Q176 42 184 50 L214 50 Q214 60 224 60 L224 570 Q214 570 214 580 L184 580 Q176 588 166 588 Q138 616 120 616 Q102 616 74 588 Q64 588 56 580 L26 580 Q26 570 16 570 L16 60 Q26 60 26 50 Z" fill="url(#panel-green)" stroke="var(--frame-line)" stroke-width="1.5"/>
    </svg>
    <div class="label__content">
      <div class="brand"><span class="brand__dot"></span>TESQUINA</div>
      <div class="title title--olio">Olio</div>
      <div class="title title--sub">extra vergine</div>
      <div class="title title--dioliva">di oliva</div>
      <div class="branch" role="img" aria-label="Illustration of an olive branch with green olives and leaves"></div>
      <div class="rule rule--top"></div>
      <div class="variant">MERIDINO</div>
      <div class="rule rule--bottom"></div>
      <div class="legal">NATIVES OLIVENÖL EXTRA<br>AUS DER EUROPÄISCHEN UNION</div>
      <div class="usage">IDEAL ZUM BRATEN</div>
      <div class="footer">
        <span>750ml℮</span><span class="footer__stars">★★</span>
        <span class="footer__sprig" role="img" aria-label="Small olive sprig ornament"></span>
        <span class="footer__stars">★★</span><span class="footer__small">BIS 220°C</span>
      </div>
    </div>
  </section>

  <!-- Red BRUMO -->
  <section class="label label--brumo-red">
    <svg class="label__frame" viewBox="0 0 240 630" aria-hidden="true">
      <defs>
        <linearGradient id="panel-red" x1="0" x2="1">
          <stop offset="0" stop-color="var(--red-b)"/><stop offset="0.5" stop-color="var(--red-a)"/><stop offset="1" stop-color="var(--red-b)"/>
        </linearGradient>
      </defs>
      <path d="M50 40 Q60 30 70 30 Q100 0 120 0 Q140 0 170 30 Q180 30 190 40 L222 40 Q222 52 234 52 L234 578 Q222 578 222 590 L190 590 Q180 600 170 600 Q140 630 120 630 Q100 630 70 600 Q60 600 50 590 L18 590 Q18 578 6 578 L6 52 Q18 52 18 40 Z" fill="var(--frame-cream)" stroke="var(--frame-line)" stroke-width="3"/>
      <path d="M56 50 Q64 42 74 42 Q102 14 120 14 Q138 14 166 42 Q176 42 184 50 L214 50 Q214 60 224 60 L224 570 Q214 570 214 580 L184 580 Q176 588 166 588 Q138 616 120 616 Q102 616 74 588 Q64 588 56 580 L26 580 Q26 570 16 570 L16 60 Q26 60 26 50 Z" fill="url(#panel-red)" stroke="var(--frame-line)" stroke-width="1.5"/>
    </svg>
    <div class="label__content">
      <div class="brand"><span class="brand__dot"></span>TESQUINA</div>
      <div class="title title--olio">Olio</div>
      <div class="title title--dioliva">di oliva</div>
      <div class="branch" role="img" aria-label="Illustration of an olive branch with yellow-green olives and leaves"></div>
      <div class="rule rule--top"></div>
      <div class="variant">BRUMO</div>
      <div class="rule rule--bottom"></div>
      <div class="legal">NATIVES OLIVENÖL EXTRA<br>AUS DER EUROPÄISCHEN UNION</div>
      <div class="usage">IDEAL ZUM BRATEN</div>
      <div class="footer">
        <span>750ml℮</span><span class="footer__stars">★★</span>
        <span class="footer__sprig" role="img" aria-label="Small olive sprig ornament"></span>
        <span class="footer__stars">★★</span><span class="footer__small">BIS 220°C</span>
      </div>
    </div>
  </section>

  <!-- Blue VELTA -->
  <section class="label label--velta-blue">
    <svg class="label__frame" viewBox="0 0 240 630" aria-hidden="true">
      <defs>
        <radialGradient id="panel-blue" cx="0.5" cy="0.45" r="0.7">
          <stop offset="0" stop-color="var(--blue-a)"/><stop offset="1" stop-color="var(--blue-b)"/>
        </radialGradient>
      </defs>
      <path d="M50 40 Q60 30 70 30 Q100 0 120 0 Q140 0 170 30 Q180 30 190 40 L222 40 Q222 52 234 52 L234 578 Q222 578 222 590 L190 590 Q180 600 170 600 Q140 630 120 630 Q100 630 70 600 Q60 600 50 590 L18 590 Q18 578 6 578 L6 52 Q18 52 18 40 Z" fill="var(--frame-cream)" stroke="var(--frame-line)" stroke-width="3"/>
      <path d="M56 50 Q64 42 74 42 Q102 14 120 14 Q138 14 166 42 Q176 42 184 50 L214 50 Q214 60 224 60 L224 570 Q214 570 214 580 L184 580 Q176 588 166 588 Q138 616 120 616 Q102 616 74 588 Q64 588 56 580 L26 580 Q26 570 16 570 L16 60 Q26 60 26 50 Z" fill="url(#panel-blue)" stroke="var(--frame-line)" stroke-width="1.5"/>
    </svg>
    <div class="label__content">
      <div class="brand"><span class="brand__dot"></span>TESQUINA</div>
      <div class="title title--olio">Olio</div>
      <div class="title title--sub">extra vergine</div>
      <div class="title title--dioliva">di oliva</div>
      <div class="branch" role="img" aria-label="Illustration of an olive branch with yellow-green olives and leaves"></div>
      <div class="rule rule--top"></div>
      <div class="variant">VELTA</div>
      <div class="rule rule--bottom"></div>
      <div class="legal">NATIVES OLIVENÖL EXTRA<br>AUS DER EUROPÄISCHEN UNION</div>
      <div class="mild">MILD</div>
      <div class="usage">IDEAL FÜR SALATE</div>
      <div class="footer">
        <span>750ml℮</span><span class="footer__stars">★★</span>
        <span class="footer__sprig" role="img" aria-label="Small olive sprig ornament"></span>
        <span class="footer__stars">★★</span><span class="footer__small">BIS 220°C</span>
      </div>
    </div>
  </section>

</main>
</body>
</html>
```